Electrical company needs professional eye catching business cards

I am an electrician who needs business cards. I have attached two images which you can use. The file ab.jpg I would atleast like to be used. The file named back.jpg can be used on the back or not... up to you.

The information on my business cards I will have displayed will be-
My name
Mobile number
web site url
Licence number
ABN

Also as another request, I would like the word "Electrician" on the front of the card somewhere. Maybe under my name or something?

Industry/Entity Type

Electrician

```html
<!DOCTYPE html>
<html lang="en">
<head>
<meta charset="utf-8">
<title>Rayline Installations – Business Card</title>
<link rel="stylesheet" href="https://fonts.googleapis.com/css2?family=Montserrat:wght@300;400;600&family=Arimo:wght@400;700&display=swap">
<style>
  :root {
    --navy-deep: #101a4a;
    --navy: #1e2f86;
    --blue: #2a44a8;
    --ink: #1f2552;
    --name-blue: #2b3378;
    --grey: #7b7b7b;
    --white: #ffffff;
    --paper: #fbfbfd;
  }
  * { margin: 0; padding: 0; box-sizing: border-box; }
  html, body { width: 1200px; height: 685px; overflow: hidden; background: var(--white); }
  .card {
    position: relative;
    width: 1200px; height: 685px;
    overflow: hidden;
    background: radial-gradient(ellipse at 45% 55%, var(--white) 40%, #eef0f4 100%);
    font-family: "Montserrat", sans-serif;
  }
  .card-shapes { position: absolute; inset: 0; }
  .brand {
    position: absolute; left: 54px; top: 32px;
    display: flex; align-items: center; gap: 12px;
    color: var(--white);
    font-family: "Montserrat", sans-serif; font-weight: 600; font-size: 42px;
    letter-spacing: -0.5px;
  }
  .brand-square { width: 40px; height: 40px; background: var(--white); border-radius: 4px; }
  .licences {
    position: absolute; right: 32px; top: 30px;
    text-align: right; color: var(--white);
    font-weight: 300; font-size: 35px; line-height: 49px;
  }
  .person {
    position: absolute; right: 770px; top: 282px;
    text-align: right; font-family: "Arimo", sans-serif;
  }
  .person-first { font-size: 42px; color: var(--name-blue); line-height: 44px; }
  .person-last { font-size: 42px; font-weight: 700; color: var(--name-blue); line-height: 44px; }
  .person-role { font-size: 32px; color: var(--grey); margin-top: 22px; line-height: 36px; }
  .person-rule {
    position: absolute; left: 20px; top: 373px; width: 410px; height: 2px;
    background: linear-gradient(90deg, rgba(43,51,120,0) 0%, var(--name-blue) 60%);
  }
  .contacts { position: absolute; left: 548px; top: 290px; list-style: none; }
  .contact {
    display: flex; align-items: center; height: 40px; margin-bottom: 39px;
    color: var(--ink); font-weight: 400; font-size: 34px;
  }
  .contact-icon { width: 44px; height: 44px; margin-right: 23px; flex: none; }
  .tagline {
    position: absolute; left: 0; right: 0; top: 605px; height: 80px;
    display: flex; align-items: center; justify-content: center;
    color: var(--white); font-size: 29px; font-weight: 400; letter-spacing: 4.2px;
  }
</style>
</head>
<body>
<main class="card">
  <svg class="card-shapes" width="1200" height="685" viewBox="0 0 1200 685" aria-hidden="true">
    <defs>
      <linearGradient id="band-top" x1="0" y1="0" x2="1" y2="0">
        <stop offset="0" stop-color="#121a3e"/>
        <stop offset="0.45" stop-color="#1f2e86"/>
        <stop offset="1" stop-color="#2a3e9e"/>
      </linearGradient>
      <linearGradient id="band-bottom" x1="0" y1="0" x2="1" y2="0">
        <stop offset="0" stop-color="#1c2a7a"/>
        <stop offset="0.5" stop-color="#2a3ea0"/>
        <stop offset="1" stop-color="#1c2a7a"/>
      </linearGradient>
    </defs>
    <path d="M0 0 H1200 V282 C1000 170 700 118 380 118 C240 118 110 122 0 128 Z" fill="url(#band-top)"/>
    <path d="M0 128 C110 122 240 118 380 118 C700 118 1000 170 1200 282 V296 C1000 186 700 134 380 134 C240 134 110 134 0 138 Z" fill="#0e163a" opacity="0.35"/>
    <rect x="0" y="605" width="1200" height="80" fill="url(#band-bottom)"/>
  </svg>

  <div class="brand"><span class="brand-square"></span>Rayline Installations</div>

  <div class="licences">
    <p>REC 20417</p>
    <p>ABN 58204163927</p>
  </div>

  <div class="person-rule"></div>
  <div class="person">
    <p class="person-first">DANIEL</p>
    <p class="person-last">WHITFORD</p>
    <p class="person-role">electrician</p>
  </div>

  <ul class="contacts">
    <li class="contact">
      <svg class="contact-icon" viewBox="0 0 44 44" aria-hidden="true">
        <rect x="11" y="1" width="22" height="42" rx="3" fill="none" stroke="#2b3378" stroke-width="3"/>
        <rect x="14" y="7" width="16" height="27" fill="#2b3378"/>
        <circle cx="22" cy="38.5" r="2" fill="#2b3378"/>
      </svg>
      725.555.0183
    </li>
    <li class="contact">
      <svg class="contact-icon" viewBox="0 0 44 44" aria-hidden="true">
        <rect x="1" y="10" width="42" height="26" fill="#2b3378"/>
        <path d="M1 10 L22 27 L43 10" fill="none" stroke="#ffffff" stroke-width="2"/>
      </svg>
      dwhitford@raylineinstall.com
    </li>
    <li class="contact">
      <svg class="contact-icon" viewBox="0 0 44 44" aria-hidden="true">
        <g fill="none" stroke="#2b3378" stroke-width="2.5">
          <circle cx="22" cy="22" r="17"/>
          <ellipse cx="22" cy="22" rx="8" ry="17"/>
          <line x1="22" y1="5" x2="22" y2="39"/>
          <line x1="5" y1="22" x2="39" y2="22"/>
          <path d="M8 13 H36 M8 31 H36"/>
        </g>
      </svg>
      www.raylineinstall.com
    </li>
  </ul>

  <p class="tagline">PROFESSIONAL QUALITY AT AN AFFORDABLE PRICE</p>
</main>
</body>
</html>
```